Etiketten für Saft-Range
grupotrinka suchte ein neues Design in der Kategorie Etiketten und hat ein Projekt auf grafikwerkstube.de gestartet.
Zielgruppe
Wir sind Getränkehersteller- und -händler. Für unsere Partner haben wir exklusive Eigenmarken, die nur unserer Partner verkaufen. Die veski Saft-Range ist eine exklusive Gastronomiemarke, die nicht im Handel erhältlich ist.
Aufgabenstellung
Das Layout unsere Eigenmarke veski soll in der Saft-Range einen Relaunch erhalten. Das ganze Sortiment besteht aktuell aus 10 Sorten. Es handelt sich um Glasflaschenetiketten, neue Stanzen beigefügt (Frontbauchetikett, Fronthalsetikett, Rückseitenetikett). Im ersten Schritt möchten wir nur die Sorten Kirsche & Apfel naturtrüb designen lassen.
Die Stanzen finden Sie beigefügt, sowie die aktuellen Layouts und Produktabbildungen der beiden genannten Sorten.
Zur Info, unsere Marke veski besteht ebenfalls aus einer Wasser-Range und Bittergetränke-Range. Die Abbildungen finden Sie zur Info ebenfalls anbei.
Folgende Bestandteile müssen auf die Etiketten (Materialfarbe weiß):
Front Bauchetikett:
- ob die Frucht als Foto oder als Zeichnung abgebildet wird ist uns erst einmal
- Marke veski
- Sorte
- Sortenzusatz wie z.B. Direktsaft
- Fruchtgehalt
- 1 l Pfandfalsche
- e - Zeichen
Rückseite:
- Marle veski
- Sortenzusatz s.o.
-Verkehrsbezeichnung
- Zutaten
- Nährwerttabelle je 100ml
- Lagerungshinweis
- 1l Pfandflasche
- Inverkehrbringeradresse
- Mindestens haltbar bis
ggf. eine Sortendifferenzierung über die Farben.
Die Glasflaschen sind klar.

```html
<!DOCTYPE html>
<html lang="de">
<head>
<meta charset="utf-8">
<title>veski Saft-Range – Etiketten</title>
<link rel="stylesheet" href="https://fonts.googleapis.com/css2?family=Nunito+Sans:wght@300;400&display=swap">
<style>
  :root {
    --page: #ffffff;
    --apple-label: #bdd005;
    --apple-fruit: #dcdc00;
    --cherry-label: #cc1a2b;
    --cherry-fruit: #e2001f;
    --ink: #ffffff;
  }
  html, body {
    margin: 0;
    padding: 0;
    background: var(--page);
    overflow: hidden;
  }
  .sheet {
    display: block;
    width: 1153px;
    height: 1200px;
  }
  .brand {
    font-family: "Nunito Sans", sans-serif;
    font-weight: 300;
    font-size: 58px;
    fill: var(--ink);
  }
  .variety {
    font-family: "Nunito Sans", sans-serif;
    font-weight: 300;
    fill: var(--ink);
  }
  .variety--neck { font-size: 27px; letter-spacing: 6px; }
  .variety--body { font-size: 39px; letter-spacing: 9px; }
  .addition {
    font-family: "Nunito Sans", sans-serif;
    font-weight: 300;
    fill: var(--ink);
  }
  .addition--neck { font-size: 15px; letter-spacing: 3px; }
  .addition--body { font-size: 22px; letter-spacing: 5px; }
  .fact {
    font-family: "Nunito Sans", sans-serif;
    font-weight: 400;
    font-size: 16px;
    fill: var(--ink);
  }
  .volume {
    font-family: "Nunito Sans", sans-serif;
    font-weight: 300;
    font-size: 26px;
    fill: var(--ink);
  }
  .deposit {
    font-family: "Nunito Sans", sans-serif;
    font-weight: 400;
    font-size: 9.5px;
    fill: var(--ink);
  }
  .label--apple { fill: var(--apple-label); }
  .label--cherry { fill: var(--cherry-label); }
  .fruit--apple { fill: var(--apple-fruit); }
  .fruit--cherry { fill: var(--cherry-fruit); }
</style>
</head>
<body>
<svg class="sheet" viewBox="0 0 1153 1200" xmlns="http://www.w3.org/2000/svg">

  <!-- Halsetikett Apfel -->
  <g class="neck-label">
    <path class="label--apple" d="M201,160 Q302,172 403,160 L462,438 Q302,474 142,438 Z"/>
    <text class="brand" x="305" y="232" text-anchor="middle">veski</text>
    <g role="img" aria-label="Illustration: grüner Apfel mit gestreiftem Trinkhalm">
      <ellipse class="fruit--apple" cx="305" cy="315" rx="54" ry="52"/>
    </g>
    <text class="variety variety--neck" x="309" y="407" text-anchor="middle">APFELSAFT</text>
    <text class="addition addition--neck" x="309" y="426" text-anchor="middle">NATURTRÜB</text>
  </g>

  <!-- Halsetikett Kirsche -->
  <g class="neck-label">
    <path class="label--cherry" d="M734,160 Q835,172 936,160 L995,438 Q835,474 675,438 Z"/>
    <text class="brand" x="838" y="232" text-anchor="middle">veski</text>
    <g role="img" aria-label="Illustration: Kirschenpaar mit Stiel, Blatt und gestreiftem Trinkhalm">
      <ellipse class="fruit--cherry" cx="850" cy="325" rx="58" ry="50"/>
    </g>
    <text class="variety variety--neck" x="844" y="414" text-anchor="middle">KIRSCHSAFT</text>
  </g>

  <!-- Bauchetikett Apfel -->
  <g class="body-label">
    <rect class="label--apple" x="101" y="609" width="402" height="443"/>
    <text class="brand" x="305" y="671" text-anchor="middle">veski</text>
    <g role="img" aria-label="Illustration: grüner Apfel mit gestreiftem Trinkhalm">
      <ellipse class="fruit--apple" cx="308" cy="808" rx="86" ry="84"/>
    </g>
    <text class="variety variety--body" x="309" y="944" text-anchor="middle">APFELSAFT</text>
    <text class="addition addition--body" x="308" y="968" text-anchor="middle">NATURTRÜB</text>
    <text class="fact" x="115" y="1019">Fruchtgehalt:</text>
    <text class="fact" x="115" y="1038">min. 50%</text>
    <text class="volume" x="493" y="1027" text-anchor="end">℮ 1,0 l</text>
    <text class="deposit" x="493" y="1041" text-anchor="end">PFANDFLASCHE</text>
  </g>

  <!-- Bauchetikett Kirsche -->
  <g class="body-label">
    <rect class="label--cherry" x="634" y="609" width="402" height="443"/>
    <text class="brand" x="835" y="671" text-anchor="middle">veski</text>
    <g role="img" aria-label="Illustration: Kirschenpaar mit Stiel, Blatt und gestreiftem Trinkhalm">
      <ellipse class="fruit--cherry" cx="850" cy="800" rx="100" ry="94"/>
    </g>
    <text class="variety variety--body" x="842" y="953" text-anchor="middle">KIRSCHSAFT</text>
    <text class="fact" x="648" y="1019">Fruchtgehalt:</text>
    <text class="fact" x="648" y="1038">min. 50%</text>
    <text class="volume" x="1026" y="1027" text-anchor="end">℮ 1,0 l</text>
    <text class="deposit" x="1026" y="1041" text-anchor="end">PFANDFLASCHE</text>
  </g>

</svg>
</body>
</html>
```